Varobel Profile Banner Design

Hi All

I would like to have a varobel profile banner design.
As I spend half my time between Zurich and Hong Kong I would like to have a Profile Banner that combines the two places.

Basic requirements:
- Image size: VaroBel banner or background photo size: 1584 x 396
- Feel: Professional but modern
- Make sure that there is nothing important that will be covered up by the varobel profile pic (left bottom)
- Should incorporate both cities (Hong Kong and Zurich)
- Text for Zurich part (city name): Zürich & (my name) "Tomas Engqvist"
- Text for Hong Kong part (City name): 香港 & (my name) "葉思恆"
- Should work well on mobile and web version of varobel

Please be creative and unique in your design.

Thanks

Tomas

Industry/Entity Type

Consulting, General business management

Requirements
Should not have
• No photo montages. Should be graphics

```html
<!DOCTYPE html>
<html lang="en">
<head>
<meta charset="utf-8">
<title>Tomas Engqvist – Zürich &amp; Hong Kong Profile Banner</title>
<link rel="stylesheet" href="https://fonts.googleapis.com/css2?family=Ubuntu:wght@700&family=Noto+Sans+TC:wght@900&display=swap">
<style>
  :root {
    --page-bg: #c9c9c9;
    --navy-deep: #03132e;
    --navy: #0a2a5e;
    --ocean: #0c4f9c;
    --zurich-blue: #0a84d6;
    --hk-red: #f20000;
    --band-red: #e60012;
    --band-blue: #0a7fd1;
    --white: #ffffff;
  }
  * { margin: 0; padding: 0; box-sizing: border-box; }
  html, body {
    width: 1174px;
    height: 1200px;
    overflow: hidden;
    background: var(--page-bg);
  }
  .banner {
    position: absolute;
    left: 37px;
    top: 462px;
    width: 1100px;
    height: 275px;
    overflow: hidden;
    background:
      radial-gradient(ellipse 40% 70% at 50% 55%, rgba(22,110,200,0.75), transparent 80%),
      linear-gradient(180deg, var(--navy) 0%, var(--navy-deep) 45%, var(--ocean) 100%);
  }
  .map-area {
    position: absolute;
    top: -10px;
    height: 295px;
  }
  .map-area--zurich {
    left: 335px;
    width: 300px;
    background: radial-gradient(ellipse 50% 50% at 50% 52%,
      rgba(10,132,214,0.95) 0%, rgba(10,132,214,0.85) 38%,
      #ffffff 56%, rgba(255,255,255,0.9) 72%, rgba(255,255,255,0) 100%);
  }
  .map-area--hongkong {
    left: 690px;
    width: 320px;
    background: radial-gradient(ellipse 50% 50% at 50% 50%,
      rgba(242,0,0,0.95) 0%, rgba(242,0,0,0.8) 36%,
      #ffffff 56%, rgba(255,255,255,0.9) 72%, rgba(255,255,255,0) 100%);
  }
  .band {
    position: absolute;
    height: 69px;
  }
  .band--zurich {
    left: 0;
    top: 52px;
    width: 290px;
    background: linear-gradient(90deg, var(--band-red) 0%, var(--band-red) 82%, rgba(230,0,18,0) 100%);
  }
  .band--hongkong {
    right: 0;
    top: 179px;
    width: 250px;
    background: linear-gradient(90deg, rgba(10,127,209,0) 0%, var(--band-blue) 12%, var(--band-blue) 100%);
  }
  .city-pill {
    position: absolute;
    height: 39px;
    border-radius: 20px;
    background: var(--white);
    display: flex;
    align-items: center;
    justify-content: center;
  }
  .city-pill--zurich {
    left: 53px;
    top: 31px;
    width: 135px;
    font-family: "Ubuntu", sans-serif;
    font-weight: 700;
    font-size: 26px;
    color: var(--zurich-blue);
  }
  .city-pill--hongkong {
    left: 913px;
    top: 157px;
    width: 134px;
    font-family: "Noto Sans TC", sans-serif;
    font-weight: 900;
    font-size: 25px;
    color: var(--hk-red);
  }
  .owner-name {
    position: absolute;
    color: var(--white);
    white-space: nowrap;
    text-align: center;
  }
  .owner-name--latin {
    left: 0;
    top: 76px;
    width: 245px;
    font-family: "Ubuntu", sans-serif;
    font-weight: 700;
    font-size: 24px;
    line-height: 34px;
  }
  .owner-name--chinese {
    left: 900px;
    top: 199px;
    width: 160px;
    font-family: "Noto Sans TC", sans-serif;
    font-weight: 900;
    font-size: 26px;
    line-height: 36px;
  }
</style>
</head>
<body>
  <section class="banner" aria-label="Profile banner combining Zürich and Hong Kong">
    <div class="map-area map-area--zurich" role="img" aria-label="Blue map of the canton of Zürich with a location marker on a white cloud backdrop"></div>
    <div class="map-area map-area--hongkong" role="img" aria-label="Red map of Hong Kong with a location marker on a white cloud backdrop"></div>

    <div class="band band--zurich"></div>
    <div class="city-pill city-pill--zurich">Zürich</div>
    <div class="owner-name owner-name--latin">Tomas Engqvist</div>

    <div class="band band--hongkong"></div>
    <div class="city-pill city-pill--hongkong" lang="zh-Hant">香港</div>
    <div class="owner-name owner-name--chinese" lang="zh-Hant">葉思恆</div>
  </section>
</body>
</html>
```